Backup Software Tri-fold Brochure Project

We need a great looking and informative brochure to describe our new Backup Software offering. The brochures are to be used in retail and small business environments given to clients interested in protecting their computer from data loss.
The brochure should include attractive imagery that conveys a sense of Trust and Security to the prospective client.
The copy is provided as an attachment to this project. We'd like our Bright Deskpoint product logo to be printed on the back cover. The logo is attached to this project.
The finished tri-fold brochure will be submitted to Plumcopy for printing as an 8.5" x 11" tri-fold brochure. Their design instructions are online http://plumcopy-example.com/custom-brochures.aspx.
The finished product should be Adobe Illustrator CS3 (*.ai) with a PDF Proof.
Target Market(s)
Retail and Small Business customers
Industry/Entity Type
Software
Designer to choose colors to be used in the design.

```html
<!DOCTYPE html>
<html lang="en">
<head>
<meta charset="utf-8">
<title>Bright Deskpoint – Offsite Backup Brochure</title>
<link rel="stylesheet" href="https://fonts.googleapis.com/css2?family=Archivo+Black&family=Open+Sans:ital,wght@0,300;0,400;0,700;1,400;1,700&display=swap">
<style>
  :root {
    --bg: #d9d9d9;
    --paper: #ffffff;
    --green: #6cbf3f;
    --green-soft: #a9d987;
    --green-pale: #e4f2d6;
    --blue: #1f63ad;
    --navy: #0b1f4d;
    --circuit: #2f5fa6;
    --ink: #1a1a1a;
  }
  * { box-sizing: border-box; margin: 0; padding: 0; }
  html, body { width: 1200px; height: 1200px; overflow: hidden; }
  body { background: var(--bg); font-family: "Open Sans", sans-serif; color: var(--ink); }

  .brochure {
    position: absolute; left: 90px; top: 200px;
    width: 1020px; height: 800px;
    display: flex;
    box-shadow: 0 14px 40px rgba(0,0,0,.25);
  }
  .panel { position: relative; width: 340px; height: 100%; overflow: hidden; background: var(--paper); }
  .panel + .panel { border-left: 1px solid rgba(0,0,0,.08); }
  .bottom-band { position: absolute; left: 0; right: 0; bottom: 0; height: 16px; background: var(--blue); }

  /* Inside panel */
  .panel--info { background: linear-gradient(180deg, var(--green-soft) 0%, var(--green-pale) 55%, #ffffff 82%); }
  .info-intro { padding: 26px 24px 14px; font-style: italic; font-size: 11.6px; line-height: 1.5; }
  .info-band {
    background: var(--blue); color: #fff; font-style: italic; font-weight: 700;
    font-size: 17px; padding: 9px 22px; margin: 4px 0 14px;
  }
  .info-heading { padding: 0 24px; font-style: italic; font-weight: 700; font-size: 14px; margin-bottom: 4px; }
  .info-body { padding: 0 24px; font-style: italic; font-size: 11.6px; line-height: 1.5; }
  .info-visual {
    position: absolute; left: 0; right: 0; bottom: 16px; height: 190px;
    background: linear-gradient(180deg, rgba(255,255,255,0) 0%, #e6ebee 45%, #cfd6dc 100%);
  }

  /* Back panel */
  .back-visual {
    position: absolute; left: 0; top: 0; width: 100%; height: 300px;
    background: radial-gradient(ellipse at 30% 40%, #5b8fd6 0%, var(--circuit) 40%, var(--navy) 100%);
  }
  .back-details {
    position: absolute; left: 0; right: 0; top: 470px; text-align: center;
  }
  .back-brand { font-weight: 700; font-size: 15px; color: var(--green); display: inline-flex; align-items: center; gap: 7px; margin-bottom: 14px; }
  .brand-square { width: 12px; height: 12px; background: var(--blue); display: inline-block; }
  .back-line { font-size: 9.5px; line-height: 1.8; color: #333; }
  .back-strip { position: absolute; left: 0; top: 300px; width: 8px; height: 484px; background: linear-gradient(180deg, var(--green), var(--green-soft)); }

  /* Cover panel */
  .cover-visual {
    position: absolute; left: 0; top: 0; width: 100%; height: 440px;
    background: radial-gradient(circle at 40% 45%, #cfe3ff 0%, #6d9ee0 10%, var(--circuit) 35%, var(--navy) 100%);
  }
  .cover-swoosh { position: absolute; left: 0; top: 380px; width: 100%; height: 110px; }
  .cover-brand {
    position: absolute; left: 36px; top: 500px;
    display: flex; align-items: center; gap: 10px;
  }
  .cover-brand .brand-square { width: 22px; height: 22px; }
  .cover-brand__name { font-weight: 700; font-size: 23px; color: var(--green); line-height: 1.1; }
  .cover-brand__tag { font-size: 10px; letter-spacing: 4px; color: var(--blue); text-transform: uppercase; margin-top: 2px; }
  .cover-headline { position: absolute; left: 36px; top: 610px; }
  .cover-headline__lead { font-family: "Archivo Black", sans-serif; font-size: 30px; color: var(--ink); line-height: 1.1; }
  .cover-headline__risk { font-weight: 300; font-size: 44px; color: var(--green); line-height: 1.1; }
</style>
</head>
<body>
<main class="brochure">

  <section class="panel panel--info">
    <p class="info-intro">Your computer stores everything you've ever created. Every list you've written, every email you've sent, movie you've made, every picture you've taken or music you've bought. Your spreadsheets, your presentations, your word files, your artwork and music, your programs are all stored on your computer. And your computer stores a copy of your personal information, your passwords and all your online banking and shopping records. Every day your digital life is at risk. Viruses, malware and hackers make it a target. A hard drive failure could wipe it out. Restoring your programs and files could cost you days of effort and potentially hundreds of dollars. But your files could be unrecoverable. This means the loss of everything you've ever created.</p>
    <h2 class="info-band">The only protection is a great backup</h2>
    <h3 class="info-heading">We Have What You Need</h3>
    <p class="info-body">We can create a snapshot of all the programs and files on your computer using our Image Backup technology. We'll give you your backup on an external hard drive which you can store someplace safe. If anything happens, just bring in your computer and your Image Backup and we'll restore your computer back to the point when the snapshot was taken. Restoring from an Image Backup is like setting your computer back in time. To make sure all your new files are protected, we'll also install Harlow-Net's Bright Deskpoint software to backup your files every night. These backups are stored in Harlow-Net's secure datacenter to protect you from even the most severe data loss scenarios. The combination of your Image Backup and your nightly backup will ensure you have complete protection for both your programs and your files. It means complete peace of mind.</p>
    <div class="info-visual" role="img" aria-label="Faded circuit board photograph"></div>
    <div class="bottom-band"></div>
  </section>

  <section class="panel panel--back">
    <div class="back-visual" role="img" aria-label="Blue circuit board photograph"></div>
    <div class="back-strip"></div>
    <div class="back-details">
      <div class="back-brand"><span class="brand-square"></span>Bright Deskpoint</div>
      <p class="back-line">http://www.harlow-example.net/backup/offsite.html</p>
      <p class="back-line">http://www.harlow-example.net/support/contact-us</p>
      <p class="back-line">Copyright © 2017 Harlow-Net, Inc. All Rights Reserved.</p>
    </div>
    <div class="bottom-band"></div>
  </section>

  <section class="panel panel--cover">
    <div class="cover-visual" role="img" aria-label="Glowing padlock on a blue circuit board"></div>
    <svg class="cover-swoosh" viewBox="0 0 340 110" preserveAspectRatio="none" aria-hidden="true">
      <path d="M0 110 L0 70 Q170 10 340 40 L340 110 Z" fill="#ffffff"/>
      <path d="M0 72 Q170 12 340 42" fill="none" stroke="#1f63ad" stroke-width="4"/>
      <path d="M0 80 Q150 30 300 40" fill="none" stroke="#6cbf3f" stroke-width="3"/>
    </svg>
    <div class="cover-brand">
      <span class="brand-square"></span>
      <div>
        <div class="cover-brand__name">Bright Deskpoint</div>
        <div class="cover-brand__tag">Offsite Backup</div>
      </div>
    </div>
    <h1 class="cover-headline">
      <span class="cover-headline__lead">Your entire digital</span><br>
      <span class="cover-headline__risk">LIFE IS AT RISK</span>
    </h1>
    <div class="bottom-band"></div>
  </section>

</main>
</body>
</html>
```